Design some Business Cards for VelmoraWear

Using my logo create a business double sided business card for me.

I want the logo in the center with the background plain and #474747

Back needs designing to house my details and tagline (if possible)

Name: Lise Karvold AICI CIP
Address: PO Box 6142. Tallowbank. Victoria. Australia. 6142
Ph: +613 9562 4830
M: 0428 196 352
S: lisekarvold

tagline: Where Fashion and Style Unite

```html
<!DOCTYPE html>
<html lang="en">
<head>
<meta charset="utf-8">
<title>VelmoraWear – Business Cards</title>
<link rel="stylesheet" href="https://fonts.googleapis.com/css2?family=Source+Sans+3:wght@400;600;700&display=swap">
<style>
  :root {
    --backdrop: #8d8e8f;
    --card: #434446;
    --pink: #d8156f;
    --pink-deep: #b8105d;
    --emblem: #6f2447;
    --emblem-ring: #8a2a56;
    --text-light: #d4d4d4;
    --text-soft: #b9b9b9;
    --text-dark: #3a3b3d;
    --white: #ffffff;
  }
  * { box-sizing: border-box; margin: 0; padding: 0; }
  html, body {
    width: 1200px; height: 899px; overflow: hidden;
    background: var(--backdrop);
    font-family: "Source Sans 3", "Helvetica Neue", Arial, sans-serif;
  }
  .canvas { position: relative; width: 1200px; height: 899px; }
  .card {
    position: absolute; top: 301px;
    width: 530px; height: 297px;
    background: var(--card);
    border-radius: 12px;
    overflow: hidden;
    box-shadow: 0 6px 18px rgba(0,0,0,0.25);
  }
  .card--front { left: 40px; }
  .card--back  { left: 630px; }

  /* Front */
  .brand {
    position: absolute; top: 78px; left: 0; right: 0;
    display: flex; justify-content: center; align-items: center; gap: 14px;
  }
  .brand__dot {
    width: 34px; height: 34px; border-radius: 50%;
    background: var(--pink);
  }
  .brand__name {
    font-size: 54px; font-weight: 400; letter-spacing: 1px;
    color: var(--text-light); line-height: 1;
  }
  .brand__slogan {
    position: absolute; top: 150px; left: 0; right: 0;
    text-align: center; font-size: 19px; letter-spacing: 4.5px;
    color: var(--text-soft);
  }
  .band {
    position: absolute; left: 0; right: 0; bottom: 0;
    height: 56px; background: var(--pink);
    border-top: 4px solid var(--pink-deep);
  }
  .band__tagline {
    display: block; text-align: center; line-height: 50px;
    color: var(--white); font-size: 21px; font-weight: 700;
  }

  /* Back */
  .details { position: absolute; top: 34px; left: 34px; color: var(--text-light); font-size: 17px; line-height: 24px; }
  .details__name { color: var(--pink); font-weight: 700; font-size: 19px; }
  .details__label { font-weight: 700; }
  .emblem { position: absolute; right: 38px; top: 60px; width: 170px; height: 170px; }
  .rule {
    position: absolute; left: 0; right: 0; bottom: 60px; height: 4px; background: var(--pink);
  }
  .band--back { height: 50px; border-top: none; }
  .band__address {
    display: block; padding-left: 30px; line-height: 50px;
    color: var(--text-dark); font-size: 20px; font-weight: 400;
  }
</style>
</head>
<body>
<div class="canvas">
  <section class="card card--front" aria-label="Business card front">
    <div class="brand">
      <span class="brand__dot"></span>
      <span class="brand__name">VelmoraWear</span>
    </div>
    <p class="brand__slogan">Ready to Wear, Perfect for You</p>
    <div class="band"><span class="band__tagline">Where Fashion and Style Unite</span></div>
  </section>

  <section class="card card--back" aria-label="Business card back">
    <div class="details">
      <p class="details__name">Lise Karvold AICI CIP</p>
      <p>Director | Harlow Estate Agents</p>
      <p>Registered Valuer 027 318</p>
      <p><span class="details__label">P:</span> +613 9562 4830</p>
      <p><span class="details__label">M:</span> 0428 196 352</p>
      <p><span class="details__label">S:</span> lisekarvold</p>
    </div>
    <svg class="emblem" viewBox="0 0 170 170" aria-hidden="true">
      <circle cx="85" cy="85" r="82" fill="var(--emblem-ring)"/>
      <circle cx="85" cy="85" r="74" fill="var(--emblem)"/>
    </svg>
    <div class="rule"></div>
    <div class="band band--back"><span class="band__address">PO Box 6142. Tallowbank. Victoria. Australia. 6142</span></div>
  </section>
</div>
</body>
</html>
```